IT Services company

we want a modern card design that combines business and technology whilst not being too loud

the Company Name is Corvane Hub and i have attached the logo

can you also put the words Smart Systems for Business under the logo

thanks

Hi can you please show the card with a web url and contact name and email and phone number please

Business

```html
<!DOCTYPE html>
<html lang="en">
<head>
<meta charset="utf-8">
<title>Corvane Hub – Business Card</title>
<link href="https://fonts.googleapis.com/css2?family=Exo+2:wght@400;600&display=swap" rel="stylesheet">
<style>
  :root {
    --backdrop: #e4e4e6;
    --brand-blue: #2e2a8c;
    --brand-red: #c8202c;
    --deep-red: #8e0f1a;
    --text-light: #ffffff;
    --title-tint: #ffd6da;
  }
  * { margin: 0; padding: 0; box-sizing: border-box; }
  html, body {
    width: 1200px; height: 750px; overflow: hidden;
    background: var(--backdrop);
    font-family: "Exo 2", sans-serif;
  }
  .business-card {
    position: absolute; left: 180px; top: 135px;
    width: 840px; height: 480px;
    border-radius: 36px; overflow: hidden;
    box-shadow: 0 10px 28px rgba(0,0,0,0.18);
  }
  .card-surface { position: absolute; inset: 0; }
  .brand-block {
    position: absolute; left: 120px; top: 104px;
    display: flex; align-items: center; gap: 22px;
  }
  .brand-mark {
    width: 82px; height: 82px; border-radius: 50%;
    background: var(--brand-red);
  }
  .brand-name {
    font-weight: 600; font-size: 56px; line-height: 1;
    color: var(--brand-blue); letter-spacing: 2px;
  }
  .brand-tagline {
    margin-top: 6px;
    font-weight: 600; font-size: 24px; color: var(--brand-blue);
    letter-spacing: 0.5px;
  }
  .contact-list {
    position: absolute; left: 540px; top: 236px;
    list-style: none; color: var(--text-light);
    font-size: 19px; line-height: 26px;
  }
  .contact-list li { display: flex; align-items: center; gap: 10px; }
  .contact-bullet {
    width: 10px; height: 10px; border-radius: 50%;
    background: var(--brand-blue); flex: none;
  }
  .holder {
    position: absolute; left: 72px; top: 352px;
    color: var(--text-light);
  }
  .holder-name { font-weight: 600; font-size: 27px; letter-spacing: 0.5px; }
  .holder-title { font-size: 16px; color: var(--title-tint); margin-left: 60px; }
</style>
</head>
<body>
  <div class="business-card">
    <svg class="card-surface" width="840" height="480" viewBox="0 0 840 480" aria-hidden="true">
      <defs>
        <linearGradient id="paper" x1="0" y1="0" x2="0" y2="1">
          <stop offset="0" stop-color="#f4f4f5"/>
          <stop offset="1" stop-color="#d9d9dc"/>
        </linearGradient>
        <linearGradient id="redField" x1="0" y1="0" x2="1" y2="1">
          <stop offset="0" stop-color="#d42833"/>
          <stop offset="0.6" stop-color="#c01d29"/>
          <stop offset="1" stop-color="#8e0f1a"/>
        </linearGradient>
      </defs>
      <rect width="840" height="480" fill="url(#paper)"/>
      <polygon points="0,300 840,168 840,480 0,480" fill="url(#redField)"/>
      <polygon points="0,292 840,160 840,170 0,302" fill="#2e2a8c"/>
    </svg>

    <div class="brand-block">
      <div class="brand-mark"></div>
      <div>
        <div class="brand-name">CORVANE HUB</div>
        <div class="brand-tagline">Smart Systems for Business</div>
      </div>
    </div>

    <ul class="contact-list">
      <li><span class="contact-bullet"></span>dana@corvanehub.com</li>
      <li><span class="contact-bullet"></span>(555) 014-2290</li>
      <li><span class="contact-bullet"></span>(555) 014-2291</li>
      <li><span class="contact-bullet"></span>www.corvanehub.com</li>
    </ul>

    <div class="holder">
      <div class="holder-name">Dana Reyes</div>
      <div class="holder-title">Director</div>
    </div>
  </div>
</body>
</html>
```